Carrowell Business Card Re-design

Our current cards are outdated. This is our website www.carrowellinsights.example. We would like something that is "on-brand" and consistent with our social media sites. We are strategic consultants with a core competency in Marketing Research. Although, please know we are considering a brand logo redesign and potentially a new look. If we like your work here we will invite you to participate when we get to that project. Thank you very much. Harriet
Here are our social sites: https://twitter.com/Carrowell?lang=en
https://plus.google.com/+Carrowellinsights
https://www.linkedin.com/company/5094827/
https://www.facebook.com/CarrowellInc/
Business

```html
<!DOCTYPE html>
<html lang="en">
<head>
<meta charset="utf-8">
<title>Carrowell Business Card</title>
<link rel="stylesheet" href="https://fonts.googleapis.com/css2?family=Open+Sans:wght@400;600;700&display=swap">
<style>
  :root {
    --bg: #e9e7e3;
    --card-white: #ffffff;
    --card-dark: #2a2a2a;
    --ink: #1f1f1f;
    --green: #8cc43f;
    --white: #ffffff;
  }
  * { margin: 0; padding: 0; box-sizing: border-box; }
  html, body {
    width: 1200px; height: 900px; overflow: hidden;
    background: var(--bg);
    font-family: "Open Sans", Arial, sans-serif;
  }
  .canvas { position: relative; width: 1200px; height: 900px; }
  .card {
    position: absolute; width: 580px; height: 332px;
    border-radius: 3px; overflow: hidden;
    box-shadow: 0 6px 18px rgba(0,0,0,0.18);
  }

  /* Back */
  .card-back { left: 570px; top: 90px; background: var(--card-dark); color: var(--white); }
  .card-back .wordmark {
    position: absolute; left: 0; right: 0; top: 88px; text-align: center;
    font-size: 60px; font-weight: 600; letter-spacing: 1px; color: var(--white);
  }
  .card-back .social {
    position: absolute; left: 0; right: 0; top: 194px; text-align: center;
    list-style: none; font-size: 14px; font-weight: 700; line-height: 21px;
  }

  /* Front */
  .card-front { left: 60px; top: 480px; background: var(--card-white); color: var(--ink); }
  .card-front .shapes { position: absolute; inset: 0; }
  .identity { position: absolute; left: 62px; top: 16px; }
  .identity .name { font-size: 20px; font-weight: 700; line-height: 24px; }
  .identity .name .first { color: var(--green); }
  .identity .role { font-size: 12px; line-height: 15px; }
  .contact {
    position: absolute; left: 30px; top: 108px;
    font-size: 14px; line-height: 20px; list-style: none;
  }
  .contact .address { margin-bottom: 4px; }
  .contact li { display: flex; align-items: center; }
  .contact svg { width: 12px; height: 12px; margin-right: 9px; flex: none; }
  .card-front .wordmark {
    position: absolute; right: 34px; top: 116px;
    font-size: 50px; font-weight: 600; color: var(--green); letter-spacing: 1px;
    white-space: nowrap;
  }
</style>
</head>
<body>
<main class="canvas">

  <section class="card card-back" aria-label="Card back">
    <div class="wordmark">Carrowell</div>
    <ul class="social">
      <li>www.chirpline.example/Carrowell?lang=en</li>
      <li>www.circlehub.example/+Carrowellinsights</li>
      <li>www.worknetwork.example/company/5094827/</li>
      <li>www.friendspace.example/CarrowellInc/</li>
    </ul>
  </section>

  <section class="card card-front" aria-label="Card front">
    <svg class="shapes" width="580" height="332" viewBox="0 0 580 332" aria-hidden="true">
      <polygon points="0,0 24,0 0,24" fill="var(--green)"/>
      <polygon points="4,52 46,12 54,12 54,52" fill="var(--ink)"/>
      <polygon points="0,258 300,258 282,280 0,280" fill="var(--green)"/>
      <polygon points="312,276 580,276 580,332 268,332" fill="var(--ink)"/>
    </svg>

    <div class="identity">
      <p class="name"><span class="first">Daniel</span> Hartley</p>
      <p class="role">Managing Director</p>
    </div>

    <ul class="contact">
      <li class="address">12345, Address Goes Here<br>Country Name, 123456.</li>
      <li>
        <svg viewBox="0 0 12 12"><path d="M2.5 1l2 2.2-1 1.3c.7 1.5 1.7 2.5 3.2 3.2l1.3-1 2.2 2-1.1 1.6C5 10 2 7 1 2.1z" fill="var(--green)"/></svg>
        044-555 018 274
      </li>
      <li>
        <svg viewBox="0 0 12 12"><rect x="1" y="2.5" width="10" height="7" fill="var(--green)"/><path d="M1 2.5l5 4 5-4" stroke="#fff" stroke-width="1" fill="none"/></svg>
        info@carrowell.example
      </li>
      <li>
        <svg viewBox="0 0 12 12"><path d="M5 7l2-2M4.2 5.5L2.8 6.9a1.8 1.8 0 002.5 2.5l1.4-1.4M7.8 6.5l1.4-1.4a1.8 1.8 0 00-2.5-2.5L5.3 4" stroke="var(--green)" stroke-width="1.4" fill="none" stroke-linecap="round"/></svg>
        www.carrowellinsights.example
      </li>
    </ul>

    <div class="wordmark">Carrowell</div>
  </section>

</main>
</body>
</html>
```